Micro-Marketing and Vending Brochure

I am looking for an elegant, fun, eye catching brochure that will highlight my new business to protential clients in the Hotel, College/University and Hospital industry. please find pictures of Micro-Markets on line and on my website, to make a fun, professional and elegant design, use color scheme from website, and logo and a few picture will be attach to this email. This is a new business and i would like to represent my company in the best possible way, please take time with this project, color, front and wording is very important along with pics. I have a image of a micro-Market please take out the BRISKO and place file logo of TORN..please let me know if more information is needed for this project to be successful

```html
<!DOCTYPE html>
<html lang="en">
<head>
<meta charset="utf-8">
<title>Orvia Markets – Micro-Market & Healthy Vending Brochure</title>
<link href="https://fonts.googleapis.com/css2?family=Arimo:wght@400;700&family=Oswald:wght@500&display=swap" rel="stylesheet">
<style>
  :root{
    --bg:#e9e9ea;
    --paper:#ffffff;
    --lavender:#dcdaec;
    --sky:#bcdcf0;
    --sky-text:#a9cdea;
    --butter:#e8c24c;
    --butter-text:#d6b33e;
    --cream:#f3efe0;
    --violet:#9585c2;
    --ink:#4a4a5a;
    --photo-green:linear-gradient(135deg,#6f9c3a 0%,#a9c95a 40%,#d2543b 70%,#eef1e6 100%);
    --photo-shelf:linear-gradient(160deg,#2b2b2b 0%,#7a3b3b 35%,#3b5f8a 65%,#1d1d1d 100%);
    --photo-shop:linear-gradient(150deg,#5a4a3c 0%,#a98f6f 50%,#3e5e8c 100%);
  }
  *{box-sizing:border-box;margin:0;padding:0}
  html,body{width:960px;height:1200px;overflow:hidden;background:var(--bg)}
  body{position:relative;font-family:"Arimo",Arial,sans-serif;color:var(--ink)}
  .page{position:absolute;background:var(--paper);overflow:hidden;box-shadow:0 2px 10px rgba(0,0,0,.08)}
  .tile{position:absolute;border-radius:8px}
  .photo{position:absolute;border-radius:10px}
  .brand{font-family:"Arimo",Arial,sans-serif;font-weight:700;color:#fff;letter-spacing:2px}

  /* back cover */
  .back-cover{left:50px;top:50px;width:420px;height:420px}
  .back-cover .slogan{position:absolute;top:90px;left:0;width:100%;text-align:center;font-family:"Oswald","Arial Narrow",sans-serif;font-weight:500;font-size:17px;line-height:22px;color:var(--sky-text);letter-spacing:.3px}
  .back-cover .contact-tile{left:145px;top:180px;width:130px;height:130px;background:var(--sky);text-align:center;padding-top:22px}
  .back-cover .brand{font-size:20px}
  .back-cover .contact{margin-top:16px;font-size:8px;line-height:13px;color:#fff}
  .back-cover .web{position:absolute;top:335px;width:100%;text-align:center;font-size:9px;color:var(--violet);letter-spacing:.5px}

  /* front cover */
  .front-cover{left:490px;top:50px;width:420px;height:420px}
  .front-cover .lav{left:32px;top:31px;width:238px;height:230px;background:var(--lavender)}
  .front-cover .sky-back{left:86px;top:191px;width:160px;height:197px;background:var(--sky);opacity:.4}
  .front-cover .cream{left:263px;top:141px;width:101px;height:166px;background:var(--cream)}
  .front-cover .salad{left:37px;top:50px;width:197px;height:196px;background:var(--photo-green)}
  .front-cover .shelf{left:241px;top:170px;width:109px;height:110px;background:var(--photo-shelf)}
  .front-cover .logo-tile{left:157px;top:256px;width:77px;height:72px;background:var(--sky);display:flex;align-items:center;justify-content:center}
  .front-cover .logo-tile .brand{font-size:14px}
  .front-cover .yellow{left:242px;top:285px;width:77px;height:76px;background:var(--butter)}
  .front-cover .headline{position:absolute;left:242px;top:72px;color:var(--butter-text)}
  .front-cover .headline .small{font-size:10px;font-weight:700;letter-spacing:.2px}
  .front-cover .headline .big{font-size:18px;line-height:21px;margin-top:4px}
  .front-cover .title{position:absolute;left:27px;top:332px;font-size:14px;font-weight:700;line-height:18px;color:var(--violet)}

  /* inner spread */
  .spread{left:60px;top:520px;width:840px;height:440px;display:flex}
  .spread .leaf{position:relative;width:420px;height:440px}
  .spread .fold{position:absolute;left:419px;top:0;width:2px;height:100%;background:linear-gradient(90deg,#dadada,#f5f5f5)}
  .quote{position:absolute;left:32px;top:32px;font-size:17px;line-height:19px;color:var(--butter-text)}
  .for-block{position:absolute;left:32px;top:86px}
  .for-block .for{font-size:40px;font-weight:700;color:var(--sky-text);line-height:40px}
  .for-block .sectors{list-style:none;font-size:11px;line-height:13px;color:var(--ink);margin-top:2px;padding-left:8px}
  .benefits{position:absolute;left:32px;top:222px;list-style:none}
  .benefits li{font-size:8.5px;font-weight:700;color:var(--violet);line-height:15px;display:flex;align-items:center;gap:5px}
  .benefits svg{width:9px;height:9px}
  .leaf-left .sky-back{left:215px;top:110px;width:160px;height:100px;background:var(--sky);opacity:.35}
  .leaf-left .yellow{left:335px;top:95px;width:55px;height:58px;background:var(--butter)}
  .leaf-left .shop1{left:272px;top:80px;width:58px;height:46px;background:var(--photo-shelf)}
  .leaf-left .shop2{left:222px;top:122px;width:56px;height:50px;background:var(--photo-shelf)}
  .leaf-left .shop3{left:280px;top:125px;width:85px;height:78px;background:var(--photo-shop)}
  .about{position:absolute;left:175px;top:272px;width:205px;font-size:9px;line-height:12px;color:var(--ink)}
  .leaf-left .badge{left:32px;top:330px;width:70px;height:70px;background:var(--sky);display:flex;align-items:center;justify-content:center}
  .leaf-left .badge .brand{font-size:12px;color:var(--violet)}
  .tagline{position:absolute;left:130px;top:360px;font-size:16px;font-weight:700;color:var(--sky-text);letter-spacing:.5px}

  .fact-label{position:absolute;left:32px;top:30px;font-size:26px;font-weight:700;color:var(--sky-text);opacity:.7;letter-spacing:1px}
  .fact-text{position:absolute;left:32px;top:68px;width:350px;font-size:9px;line-height:12px;color:var(--ink)}
  .leaf-right .fridges{left:32px;top:140px;width:220px;height:260px;background:var(--photo-shelf)}
  .leaf-right .callout{left:200px;top:170px;width:185px;height:175px;background:var(--butter);padding:20px 18px;font-size:10px;line-height:14px;color:#fff}
</style>
</head>
<body>

<section class="page back-cover">
  <p class="slogan">LETS MAKE A CHANGE<br>AND BECOME<br>HEALTHY, HAPPY SNACK PEOPLE</p>
  <div class="tile contact-tile">
    <div class="brand">ORVIA</div>
    <div class="contact">Orvia Markets LLC<br>(555) 014-2290<br>info@orviamarkets.com</div>
  </div>
  <p class="web">WWW.ORVIAMARKETS.COM</p>
</section>

<section class="page front-cover">
  <div class="tile lav"></div>
  <div class="tile sky-back"></div>
  <div class="tile cream"></div>
  <div class="photo salad" role="img" aria-label="Fresh Greek salad with cucumber, tomato, feta and olives"></div>
  <div class="photo shelf" role="img" aria-label="Micro-market shelves stocked with snacks and a self-checkout kiosk"></div>
  <div class="tile logo-tile"><span class="brand">ORVIA</span></div>
  <div class="tile yellow"></div>
  <div class="headline">
    <div class="small">THE MOST RADICAL CHANGE</div>
    <div class="big">IN AT-WORK<br>FOOD SERVICE</div>
  </div>
  <h1 class="title">Micro-Market &amp;<br>Healthy Vending Solution</h1>
</section>

<section class="page spread">
  <div class="leaf leaf-left">
    <p class="quote">“Healthy,<br>&nbsp;Happy Snack People”</p>
    <div class="for-block">
      <div class="for">FOR</div>
      <ul class="sectors"><li>Hotels</li><li>Colleges and Universities</li><li>Hospitals</li></ul>
    </div>
    <div class="tile sky-back"></div>
    <div class="tile yellow"></div>
    <div class="photo shop1" role="img" aria-label="Micro-market snack display"></div>
    <div class="photo shop2" role="img" aria-label="Refrigerated drink coolers"></div>
    <div class="photo shop3" role="img" aria-label="Customer shopping at a micro-market"></div>
    <ul class="benefits">
      <li><svg viewBox="0 0 10 10"><path d="M1 5l3 3 5-7" fill="none" stroke="#9585c2" stroke-width="2"/></svg>Boost Employee/Clients/ patients Morale</li>
      <li><svg viewBox="0 0 10 10"><path d="M1 5l3 3 5-7" fill="none" stroke="#9585c2" stroke-width="2"/></svg>Increase Productivity</li>
      <li><svg viewBox="0 0 10 10"><path d="M1 5l3 3 5-7" fill="none" stroke="#9585c2" stroke-width="2"/></svg>Support employee Healthy lifestyle</li>
    </ul>
    <p class="about">Orvia Markets LLC Micro-Markets and Vending system allows you to select from hundreds of healthy, tasty and nutritional balance options. We have healthy snack and fresh produce</p>
    <div class="tile badge"><span class="brand">ORVIA</span></div>
    <p class="tagline">Easy Convenient Healthy</p>
  </div>
  <div class="leaf leaf-right">
    <p class="fact-label">FACT</p>
    <p class="fact-text">Nearly one third of adults are considered obese, and poor diet lowers focus and productivity at the office, school and home, costing employers thousands each year.</p>
    <div class="photo fridges" role="img" aria-label="Row of micro-market coolers stocked with fresh food and drinks"></div>
    <div class="tile callout">Our micro-markets stock fresh salads, fruit, yogurt and wholesome snacks, open around the clock with simple self checkout by card or phone.</div>
  </div>
  <div class="fold"></div>
</section>

</body>
</html>
```